Web Design Project for DJ

We need a web design for a DJ. Our client is a freelance DJ who already has a regular gig at a major night club but is looking to expand his exposure. He is located in a major metropolitan area and is looking for further gigs. He is hoping to generate further business via the website, including bookings via the site.

For reference his pagelinker page is here https://www.pagelinker.example/pages/DJ-Vorn/730162948415207

Following face to face discussions with the client today we have made a few small alterations to the brief.  We are hoping to have some images uploaded shortly.

Target Market(s)

Event planners, night club owners, radio stations, younger age groups (16-35)

Industry/Entity Type

Business

Requirements
Must have
• Name is DJVorn, this should obviously feature prominently. His current business card is attached as an example.

Links to Pagelinker and Tunedrift

Cool, modern look, slightly edgy.

Site will be built in Joomla, so a front page and secondary page template is required.
Nice to have
• Blog style layout to front page featuring recent and upcoming gigs.

Secondary pages may include a more expansive blog, a list of upcoming gigs, and a booking form.

Darker colour palettes preferred and use of same/similar fonts to those on the business card are an obvious plus

```html
<!DOCTYPE html>
<html lang="en">
<head>
<meta charset="utf-8">
<title>DJVorn — Home</title>
<link href="https://fonts.googleapis.com/css2?family=Open+Sans:wght@400;600;700&family=Arimo:wght@400;700&display=swap" rel="stylesheet">
<style>
:root{
  --sidebar:#2a2c38;
  --sidebar-line:#3b3e4c;
  --logo-bg:#000;
  --stage-deep:#1f2266;
  --stage-mid:#2f3592;
  --stage-glow:#5f78d8;
  --panel:#d7d7f0;
  --panel-edge:#eeeefb;
  --accent:#4aa3e0;
  --accent-dark:#2f84c4;
  --ink:#111;
  --ink-soft:#333;
  --green:#4f9a1c;
  --link-green:#5e9b23;
  --nav-text:#d9dbe6;
  --muted:#c9cbd6;
}
*{box-sizing:border-box;margin:0;padding:0}
html,body{width:1077px;height:1200px;overflow:hidden}
body{position:relative;font-family:"Arimo",Arial,sans-serif;color:var(--ink);
  background:radial-gradient(ellipse 380px 420px at 660px 600px,var(--stage-glow),var(--stage-mid) 55%,var(--stage-deep) 100%);}
.abs{position:absolute}

/* sidebar */
.sidebar{left:0;top:0;width:260px;height:1200px;background:var(--sidebar);overflow:hidden}
.brand{left:0;top:0;width:260px;height:135px;background:var(--logo-bg);display:flex;align-items:center;justify-content:center;
  font-family:"Open Sans",sans-serif;font-weight:700;font-size:44px;color:#fff;letter-spacing:1px}
.nav-item{left:70px;font-family:"Open Sans",sans-serif;font-weight:700;font-size:11px;color:var(--nav-text);display:flex;align-items:center;gap:8px;white-space:nowrap}
.nav-item svg{width:15px;height:15px;fill:var(--nav-text)}
.nav-active{left:63px;top:150px;width:210px;height:23px;background:linear-gradient(var(--accent),var(--accent-dark));
  clip-path:polygon(0 0,96% 0,100% 50%,96% 100%,0 100%);padding-left:10px;color:#e6f3ff}
.nav-active svg{fill:#9fd0f3}
.rule{left:0;width:260px;height:1px;background:var(--sidebar-line)}
.player{left:36px;top:478px;width:214px;height:26px;display:flex;align-items:center;gap:5px}
.ctl{width:15px;height:15px;border-radius:50%;background:#1b1c25;border:1px solid #555;flex:none}
.ctl-play{width:22px;height:22px;border-radius:50%;background:radial-gradient(#6cc0ff,var(--accent-dark));border:1px solid #1e5d8f;flex:none}
.track{flex:1;height:7px;border-radius:4px;background:#15161d;border:1px solid #555;position:relative;margin:0 8px 0 4px}
.track::before{content:"";position:absolute;left:-2px;top:-4px;width:12px;height:12px;border-radius:50%;background:#ddd}
.ctl-vol{width:14px;height:12px;border-radius:2px;background:#1b1c25;border:1px solid #555;flex:none}
.now-playing{left:36px;top:516px;font-family:"Open Sans",sans-serif;font-weight:600;font-size:11px;color:#e0e2ea;white-space:nowrap}
.touch-label{left:36px;top:551px;font-family:"Open Sans",sans-serif;font-weight:600;font-size:10px;color:#e0e2ea;white-space:nowrap}
.touch-links{left:36px;top:566px;width:220px;font-family:"Open Sans",sans-serif;font-weight:600;font-size:9px;color:#fff;display:flex;gap:8px;white-space:nowrap}
.copyright{left:36px;top:602px;font-family:"Open Sans",sans-serif;font-weight:600;font-size:10px;color:#c8cad4;white-space:nowrap}

/* panels */
.panel{background:var(--panel);border-radius:6px;box-shadow:0 0 0 1px var(--panel-edge) inset}
.slider{left:287px;top:21px;width:763px;height:332px}
.slide{left:12px;top:12px;width:739px;height:308px;background:radial-gradient(ellipse at 60% 45%,#2a3a8a,#080818 70%)}
.slide-name{left:44px;top:60px;font-family:"Open Sans",sans-serif;font-weight:700;font-size:48px;color:#fff}
.slide-arrow{top:140px;width:16px;height:28px;stroke:#fff;stroke-width:3;fill:none}
.dots{right:18px;bottom:6px;display:flex;gap:3px}
.dots i{width:7px;height:7px;border-radius:50%;background:#fff}

.ribbon{top:9px;height:19px;left:50px;right:50px}
.ribbon svg{position:absolute;inset:0;width:100%;height:100%}
.ribbon span{position:relative;display:block;text-align:center;font-family:"Open Sans",sans-serif;font-weight:700;font-size:11px;line-height:19px;color:#fff;white-space:nowrap}

.gigs{left:287px;top:377px;width:370px;height:331px}
.releases{left:680px;top:377px;width:370px;height:331px}
.gig{left:16px;width:300px;height:62px}
.date{left:0;top:0;width:46px;height:44px;background:#fff;border-radius:3px;border:1px solid #b9bbd0;text-align:center;font-size:11px;color:var(--accent-dark);padding-top:6px;line-height:18px}
.date::after{content:"";position:absolute;left:0;right:0;top:22px;height:1px;background:#ccd}
.gig-title{left:65px;top:0;font-size:11px;white-space:nowrap}
.gig-detail{left:65px;top:19px;font-size:11px;color:var(--ink-soft);white-space:nowrap}
.gig-links{left:65px;top:37px;font-size:9px;font-weight:700;color:var(--green);display:flex;gap:18px;white-space:nowrap}
.gig-rule{left:0;top:56px;width:295px;height:1px;background:linear-gradient(90deg,#b4b6cc,transparent)}
.wide-btn{height:31px;border-radius:4px;background:linear-gradient(#eef0fb,#c3c6dd);border:1px solid #a9abc4;
  font-family:"Open Sans",sans-serif;font-weight:600;font-size:11px;color:#3c3e52;display:flex;align-items:center;justify-content:center}

.release{left:16px;width:330px;height:62px}
.thumb{border:2px solid #fff;box-shadow:0 0 0 1px #9a9cb4}
.rel-thumb{left:0;top:0;width:78px;height:58px}
.rel-title{left:86px;top:1px;font-size:14px;font-weight:700;white-space:nowrap}
.rel-line{left:86px;font-size:11px;color:var(--ink-soft);white-space:nowrap}
.pill{left:254px;width:74px;height:16px;border-radius:8px;background:linear-gradient(#f4f6ff,#c9d9ea);border:1px solid #8fb6d4;
  font-family:"Open Sans",sans-serif;font-weight:700;font-size:7.5px;color:#4c6d8a;display:flex;align-items:center;justify-content:center;gap:4px;white-space:nowrap}
.badge-new{left:-10px;top:-10px;width:30px;height:22px;border-radius:50%;background:#c4281b;color:#fff;font-size:8px;font-weight:700;display:flex;align-items:center;justify-content:center}

.post{left:287px;width:527px;height:133px}
.post-thumb{left:16px;top:17px;width:100px;height:100px}
.post-title{left:134px;top:23px;font-size:17px;font-weight:700;white-space:nowrap}
.meta{top:27px;font-size:9px;color:var(--ink-soft);text-decoration:underline;display:flex;align-items:center;gap:5px;white-space:nowrap}
.meta svg{width:11px;height:11px;fill:#222}
.post-body{left:132px;top:55px;width:368px;font-size:11.5px;line-height:17px;color:var(--ink-soft)}
.more{color:var(--link-green);font-size:12.5px;margin-left:6px}

.social-box{left:837px;top:733px;width:211px;height:259px}
.fb-card{left:8px;top:44px;width:195px;height:205px;background:#fff}
.fb-avatar{left:7px;top:7px;width:55px;height:50px}
.fb-name{left:68px;top:10px;font-size:13px;font-weight:700;color:#3b5998;white-space:nowrap}
.fb-like{left:68px;top:30px;width:78px;height:22px;border:1px solid #aab;border-radius:2px;background:#eef0f6;font-size:11px;color:#3b5998;display:flex;align-items:center;justify-content:center}
.fb-count{left:8px;top:73px;font-size:11px;color:#333;white-space:nowrap}
.fb-count em{font-style:normal;color:#3b5998}
.fans{left:8px;top:97px;width:175px;display:grid;grid-template-columns:repeat(3,53px);gap:4px 5px}
.fans div{height:50px}
.track-box{left:840px;top:1014px;width:210px;height:168px}
.track-card{left:4px;top:4px;width:202px;height:160px;background:#f2f2f4;border-radius:3px}
.tc-play{left:12px;top:12px;width:30px;height:30px;border-radius:50%;background:#e2322a}
.tc-user{left:50px;top:16px;font-size:8px;color:#666;white-space:nowrap}
.tc-title{left:50px;top:27px;font-size:9.5px;font-weight:700;color:#222;white-space:nowrap}
.wave{left:8px;top:50px;width:188px;height:38px;background:repeating-linear-gradient(90deg,#555 0 1px,transparent 1px 3px);opacity:.7}
.tc-stats{left:10px;top:98px;font-size:7px;color:#888;display:flex;gap:10px;white-space:nowrap}
</style>
</head>
<body>

<aside class="abs sidebar">
  <div class="abs brand">DJVorn</div>

  <nav>
    <div class="abs nav-item nav-active"><svg viewBox="0 0 16 16"><path d="M8 2 1 8h2v6h4v-4h2v4h4V8h2z"/></svg>Home</div>
    <div class="abs nav-item" style="top:197px"><svg viewBox="0 0 16 16"><rect x="1" y="3" width="14" height="11" rx="1"/></svg>Biography</div>
    <div class="abs nav-item" style="top:239px"><svg viewBox="0 0 16 16"><circle cx="8" cy="8" r="7"/><circle cx="8" cy="8" r="2" fill="#2a2c38"/></svg>Discography</div>
    <div class="abs nav-item" style="top:283px"><svg viewBox="0 0 16 16"><rect x="3" y="2" width="10" height="13" rx="1"/></svg>Gigs</div>
    <div class="abs nav-item" style="top:323px"><svg viewBox="0 0 16 16"><rect x="1" y="3" width="14" height="10"/><path d="M2 12l4-5 3 3 2-2 4 4z" fill="#2a2c38"/></svg>Media</div>
    <div class="abs nav-item" style="top:363px"><svg viewBox="0 0 16 16"><ellipse cx="7" cy="7" rx="6" ry="4.5"/><path d="M3 10l-1 4 4-3z"/></svg>Contact</div>
    <div class="abs nav-item" style="top:403px"><svg viewBox="0 0 16 16"><circle cx="8" cy="8" r="7"/><rect x="7" y="7" width="2" height="5" fill="#2a2c38"/><rect x="7" y="4" width="2" height="2" fill="#2a2c38"/></svg>Template Features</div>
  </nav>

  <div class="abs rule" style="top:465px"></div>
  <div class="abs player">
    <span class="ctl"></span><span class="ctl-play"></span><span class="ctl"></span>
    <span class="track"></span><span class="ctl-vol"></span>
  </div>
  <div class="abs now-playing">☰&nbsp; Nalto - 7th Gate</div>
  <div class="abs rule" style="top:543px"></div>
  <div class="abs touch-label">STAY IN TOUCH:</div>
  <div class="abs touch-links"><span>Pagelinker</span><span>Chirper</span><span>Circles</span><span>Tunedrift</span></div>
  <div class="abs rule" style="top:585px"></div>
  <div class="abs copyright">© 2013 DJVORN, ALL RIGHTS RESERVED.</div>
</aside>

<main>
  <section class="abs panel slider">
    <div class="abs slide" role="img" aria-label="DJ performing at turntables on a dark stage under blue light">
      <div class="abs slide-name">DJVorn</div>
      <svg class="abs slide-arrow" style="left:8px" viewBox="0 0 16 28"><path d="M13 3 3 14l10 11"/></svg>
      <svg class="abs slide-arrow" style="right:8px" viewBox="0 0 16 28"><path d="M3 3l10 11L3 25"/></svg>
      <div class="abs dots"><i></i><i></i><i></i></div>
    </div>
  </section>

  <section class="abs panel gigs">
    <div class="abs ribbon"><svg viewBox="0 0 270 19" preserveAspectRatio="none"><path d="M0 2h270l-8 8 8 8H0l8-8z" fill="#5da8e0"/><rect x="28" y="0" width="214" height="19" rx="9.5" fill="#4a9ad8" stroke="#e8f3fc" stroke-width="1"/></svg><span>UPCOMING GIGS</span></div>

    <div class="abs gig" style="top:50px">
      <div class="abs date">09<br>MAY</div>
      <div class="abs gig-title">Miami - Discoteca</div>
      <div class="abs gig-detail">03:00-06:00 | Venue address: Harbor Street</div>
      <div class="abs gig-links"><span>BUY TICKET</span><span>WIEW FLYER</span></div>
      <div class="abs gig-rule"></div>
    </div>
    <div class="abs gig" style="top:133px">
      <div class="abs date">09<br>MAY</div>
      <div class="abs gig-title">Miami - Discoteca</div>
      <div class="abs gig-detail">03:00-06:00 | Venue address: Harbor Street</div>
      <div class="abs gig-links"><span>BUY TICKET</span><span>WIEW FLYER</span></div>
      <div class="abs gig-rule"></div>
    </div>
    <div class="abs gig" style="top:219px">
      <div class="abs date">09<br>MAY</div>
      <div class="abs gig-title">Miami - Discoteca</div>
      <div class="abs gig-detail">03:00-06:00 | Venue address: Harbor Street</div>
      <div class="abs gig-links"><span>BUY TICKET</span><span>WIEW FLYER</span></div>
      <div class="abs gig-rule"></div>
    </div>
    <div class="abs wide-btn" style="left:15px;top:296px;width:340px">COMPLETE SCHEDULE</div>
  </section>

  <section class="abs panel releases">
    <div class="abs ribbon"><svg viewBox="0 0 270 19" preserveAspectRatio="none"><path d="M0 2h270l-8 8 8 8H0l8-8z" fill="#5da8e0"/><rect x="28" y="0" width="214" height="19" rx="9.5" fill="#4a9ad8" stroke="#e8f3fc" stroke-width="1"/></svg><span>NEW RELEASES</span></div>

    <div class="abs release" style="top:55px">
      <div class="abs thumb rel-thumb" role="img" aria-label="Release cover with warm club lights" style="background:linear-gradient(135deg,#6a3a8a,#d89a4a,#3a2a6a)"></div>
      <div class="abs rel-title">La Kazan</div>
      <div class="abs rel-line" style="top:25px">Nalto</div>
      <div class="abs rel-line" style="top:45px">Label DJVorn</div>
      <div class="abs pill" style="top:11px">PLAY NOW ▸</div>
      <div class="abs pill" style="top:41px">BUY NOW ▾</div>
    </div>
    <div class="abs release" style="top:135px">
      <div class="abs thumb rel-thumb" role="img" aria-label="Release cover with golden stage glow" style="background:linear-gradient(135deg,#3a2a5a,#c8a060,#2a2040)"></div>
      <div class="abs badge-new">NEW</div>
      <div class="abs rel-title">Beyond the Horizon</div>
      <div class="abs rel-line" style="top:25px">Nalto</div>
      <div class="abs rel-line" style="top:45px">Label DJVorn</div>
      <div class="abs pill" style="top:13px">PLAY NOW ▸</div>
      <div class="abs pill" style="top:43px">BUY NOW ▾</div>
    </div>
    <div class="abs release" style="top:215px">
      <div class="abs thumb rel-thumb" role="img" aria-label="Release cover with crowd under party lights" style="background:linear-gradient(135deg,#2a3a5a,#a07050,#4a3a6a)"></div>
      <div class="abs rel-title">Happy Vibes</div>
      <div class="abs rel-line" style="top:25px">Nalto</div>
      <div class="abs rel-line" style="top:45px">Label DJVorn</div>
      <div class="abs pill" style="top:8px">PLAY NOW ▸</div>
      <div class="abs pill" style="top:38px">BUY NOW ▾</div>
    </div>
    <div class="abs wide-btn" style="left:15px;top:296px;width:342px">VIEW ALL RELEASES</div>
  </section>

  <article class="abs panel post" style="top:733px">
    <div class="abs thumb post-thumb" role="img" aria-label="Club night event flyer in blue tones" style="background:linear-gradient(135deg,#1a3a6a,#5a8ab8,#1a2a4a)"></div>
    <h2 class="abs post-title">Beyond the Horizon</h2>
    <div class="abs meta" style="left:308px"><svg viewBox="0 0 12 12"><circle cx="6" cy="3.5" r="3"/><path d="M0 12c0-4 3-5 6-5s6 1 6 5z"/></svg>DjVORN</div>
    <div class="abs meta" style="left:379px"><svg viewBox="0 0 12 12"><circle cx="6" cy="6" r="5" fill="none" stroke="#222" stroke-width="1.5"/><path d="M6 3v3h2" stroke="#222" fill="none"/></svg>2 MAY 2013</div>
    <div class="abs meta" style="left:472px"><svg viewBox="0 0 12 12"><ellipse cx="6" cy="5" rx="5.5" ry="4"/><path d="M2 8 1 11l4-2z"/></svg>3</div>
    <p class="abs post-body">“The best way to sum up this year's event is to say we didthis event as a community instead of it being just one promoter. “The best way to sum up this year's event is to say we didthis event as a community...<span class="more">More...</span></p>
  </article>

  <article class="abs panel post" style="top:891px">
    <div class="abs thumb post-thumb" role="img" aria-label="Club night event flyer in violet and cyan" style="background:linear-gradient(135deg,#3a3a7a,#7ab0d0,#2a2a5a)"></div>
    <h2 class="abs post-title">La Kazan</h2>
    <div class="abs meta" style="left:308px"><svg viewBox="0 0 12 12"><circle cx="6" cy="3.5" r="3"/><path d="M0 12c0-4 3-5 6-5s6 1 6 5z"/></svg>DjVORN</div>
    <div class="abs meta" style="left:379px"><svg viewBox="0 0 12 12"><circle cx="6" cy="6" r="5" fill="none" stroke="#222" stroke-width="1.5"/><path d="M6 3v3h2" stroke="#222" fill="none"/></svg>2 MAY 2013</div>
    <div class="abs meta" style="left:472px"><svg viewBox="0 0 12 12"><ellipse cx="6" cy="5" rx="5.5" ry="4"/><path d="M2 8 1 11l4-2z"/></svg>3</div>
    <p class="abs post-body">“The best way to sum up this year's event is to say we didthis event as a community instead of it being just one promoter. “The best way to sum up this year's event is to say we didthis event as a community...<span class="more">More...</span></p>
  </article>

  <article class="abs panel post" style="top:1049px">
    <div class="abs thumb post-thumb" role="img" aria-label="Colourful club party event flyer" style="background:linear-gradient(135deg,#d04a7a,#e8b040,#4a6ad0)"></div>
    <h2 class="abs post-title">Happy Vibes</h2>
    <div class="abs meta" style="left:308px"><svg viewBox="0 0 12 12"><circle cx="6" cy="3.5" r="3"/><path d="M0 12c0-4 3-5 6-5s6 1 6 5z"/></svg>DjVORN</div>
    <div class="abs meta" style="left:379px"><svg viewBox="0 0 12 12"><circle cx="6" cy="6" r="5" fill="none" stroke="#222" stroke-width="1.5"/><path d="M6 3v3h2" stroke="#222" fill="none"/></svg>2 MAY 2013</div>
    <div class="abs meta" style="left:472px"><svg viewBox="0 0 12 12"><ellipse cx="6" cy="5" rx="5.5" ry="4"/><path d="M2 8 1 11l4-2z"/></svg>3</div>
    <p class="abs post-body">“The best way to sum up this year's event is to say we didthis event as a community instead of it being just one promoter. “The best way to sum up this year's event is to say we didthis event as a community...<span class="more">More...</span></p>
  </article>

  <aside class="abs panel social-box">
    <div class="abs ribbon" style="left:4px;right:0;top:12px"><svg viewBox="0 0 205 19" preserveAspectRatio="none"><path d="M0 2h205l-7 8 7 8H0l7-8z" fill="#5da8e0"/><rect x="20" y="0" width="165" height="19" rx="9.5" fill="#4a9ad8" stroke="#e8f3fc" stroke-width="1"/></svg><span style="font-size:10px">DJVorn on Pagelinker</span></div>
    <div class="abs fb-card">
      <div class="abs fb-avatar" role="img" aria-label="Profile photo" style="background:linear-gradient(135deg,#4a3a30,#8a6a50)"></div>
      <div class="abs fb-name">DJ Vorn</div>
      <div class="abs fb-like">Îmi place</div>
      <div class="abs fb-count">146 de persoane apreciază <em>DJ Vorn</em>.</div>
      <div class="abs fans" role="img" aria-label="Grid of fan profile photos">
        <div style="background:#8a5a4a"></div><div style="background:#b86a3a"></div><div style="background:#6a7a8a"></div>
        <div style="background:#5a3a2a"></div><div style="background:#7a7a80"></div><div style="background:#6a8a6a"></div>
      </div>
    </div>
  </aside>

  <aside class="abs panel track-box">
    <div class="abs track-card">
      <div class="abs tc-play"></div>
      <svg class="abs" style="left:24px;top:20px" width="10" height="14" viewBox="0 0 10 14"><path d="M0 0l10 7-10 7z" fill="#fff"/></svg>
      <div class="abs tc-user">officialnordichouse...</div>
      <div class="abs tc-title">Nordic House ...</div>
      <div class="abs wave" role="img" aria-label="Track waveform"></div>
      <div class="abs tc-stats"><span>▸ 1,636,894</span><span>♥ 33,775</span><span>Tunedrift</span></div>
    </div>
  </aside>
</main>

</body>
</html>
```